International Wine Label 202001

Need a wine label designed for several new wines from California being exported to Asia. This label should be focused around an animal theme of the flowing: Tiger, Lion, Horse or Eagle. The label should be adaptable to a product line of wines. For example the label could be used for a Cabernet wine, Merlot, Chardonnay or Pinot. A slight modification to the label design should be incorporated to allow for the different varietals. Front label design only. Can utilize photo image in design.
The label would be around 5.75" x 3.50".

Target Market(s)

25-35 year old wine buyers in the global market

Industry/Entity Type

Retail

Font styles to use
Sans Serif

Requirements
Must have
• Wine name based on design (designer suggest name)
Wine varietals
Vintage date
Additional wording area
Nice to have
• Rectangular label preferred Front label only.

```html
<!DOCTYPE html>
<html lang="en">
<head>
<meta charset="utf-8">
<title>Ember Crest – Cabernet Sauvignon Label</title>
<link rel="stylesheet" href="https://fonts.googleapis.com/css2?family=Montserrat:wght@600;800&display=swap">
<style>
  :root {
    --page: #f2efea;
    --label-light: #a3a08c;
    --label-mid: #7d7b68;
    --label-dark: #3f3f33;
    --frame: #2c2c24;
    --text-light: #f4f3ee;
    --brand: #2a2622;
    --accent-red: #b3201c;
    --tiger-orange: #c98a3a;
    --tiger-cream: #e8e2d2;
    --tiger-shade: #5c5a4c;
  }
  * { margin: 0; padding: 0; box-sizing: border-box; }
  html, body {
    width: 1200px; height: 789px; overflow: hidden;
    background: var(--page);
    font-family: "Montserrat", Arial, sans-serif;
  }
  .canvas {
    width: 1200px; height: 789px;
    display: flex; align-items: center; justify-content: center;
  }
  .wine-label {
    position: relative;
    width: 1036px; height: 630px;
    border-radius: 14px;
    border: 3px solid var(--frame);
    background: radial-gradient(ellipse at 50% 40%, var(--label-light) 0%, var(--label-mid) 55%, var(--label-dark) 100%);
    overflow: hidden;
    display: flex; flex-direction: column; align-items: center;
    color: var(--text-light);
  }
  .brand-name {
    margin-top: 44px;
    font-weight: 800;
    font-size: 62px;
    line-height: 1;
    color: var(--brand);
    letter-spacing: 1px;
    display: flex; align-items: center; gap: 18px;
  }
  .brand-mark {
    width: 18px; height: 18px; border-radius: 50%;
    background: var(--accent-red);
  }
  .tiger-art {
    margin-top: 28px;
    width: 330px; height: 240px;
    border-radius: 48% 52% 30% 30% / 55% 55% 30% 30%;
    background: linear-gradient(160deg, var(--tiger-cream) 0%, var(--tiger-orange) 55%, var(--tiger-shade) 100%);
  }
  .varietal {
    margin-top: 34px;
    font-weight: 800;
    font-size: 46px;
    line-height: 1.2;
    letter-spacing: 2px;
    text-transform: uppercase;
  }
  .region {
    margin-top: 8px;
    font-weight: 600;
    font-size: 30px;
    line-height: 1.2;
    letter-spacing: 3px;
    text-transform: uppercase;
  }
  .vintage {
    margin-top: 8px;
    font-weight: 800;
    font-size: 48px;
    line-height: 1.2;
    letter-spacing: 3px;
  }
</style>
</head>
<body>
<main class="canvas">
  <section class="wine-label">
    <h1 class="brand-name"><span class="brand-mark"></span>Ember Crest</h1>
    <div class="tiger-art" role="img" aria-label="Illustration of a reclining tiger"></div>
    <p class="varietal">Cabernet Sauvignon</p>
    <p class="region">California Napa Valley</p>
    <p class="vintage">2020</p>
  </section>
</main>
</body>
</html>
```